Redesign my business cards

I would like pretty much all the same information as my current business cards but redesigned to stand out more and be more unique photo uploaded to show my current business cards don’t mind if you want to remove or replace I for on the back

```html
<!DOCTYPE html>
<html lang="en">
<head>
<meta charset="utf-8">
<title>Shoreline Detailing – Business Card</title>
<link href="https://fonts.googleapis.com/css2?family=Arimo:ital,wght@0,400;0,700;1,700&display=swap" rel="stylesheet">
<style>
  :root {
    --page: #e6e6e6;
    --navy: #061f2d;
    --navy-mid: #0a2f42;
    --teal-line: rgba(60, 196, 230, 0.16);
    --violet: #8a2bd6;
    --violet-light: #b57cff;
    --crimson: #e0294a;
    --cyan: #3cc4e6;
    --white: #ffffff;
    --soft: #b9d3df;
    --divider: rgba(159, 195, 212, 0.22);
  }
  * { margin: 0; padding: 0; box-sizing: border-box; }
  html, body { width: 1200px; height: 1200px; overflow: hidden; }
  body {
    background: var(--page);
    font-family: "Arimo", Arial, sans-serif;
    position: relative;
  }
  .card {
    position: absolute;
    left: 257px;
    width: 686px;
    height: 392px;
    border-radius: 26px;
    overflow: hidden;
    background: linear-gradient(135deg, var(--navy-mid) 0%, var(--navy) 70%);
  }
  .card--front { top: 150px; }
  .card--back { top: 658px; }

  .accent-band {
    position: absolute; left: 0; top: 0; bottom: 0; width: 14px;
    background: linear-gradient(180deg, var(--violet), var(--crimson));
  }
  .stripes { position: absolute; right: 0; top: 0; width: 300px; height: 392px; }

  /* front */
  .brand {
    position: absolute; left: 52px; top: 44px;
    display: flex; align-items: center; gap: 12px;
  }
  .brand-dot { width: 16px; height: 16px; border-radius: 50%; background: var(--cyan); }
  .brand-name { font-size: 15px; font-weight: 700; letter-spacing: 3px; color: var(--violet-light); }

  .owner-name {
    position: absolute; left: 52px; top: 138px;
    font-size: 44px; font-weight: 700; color: var(--white); letter-spacing: 1px;
  }
  .owner-role {
    position: absolute; left: 54px; top: 196px;
    font-size: 15px; font-weight: 700; color: var(--crimson);
    letter-spacing: 4px; text-transform: uppercase;
  }
  .name-rule {
    position: absolute; left: 54px; top: 232px; width: 300px; height: 3px;
    border-radius: 2px;
    background: linear-gradient(90deg, var(--violet), var(--crimson));
  }
  .contacts {
    position: absolute; left: 52px; top: 276px;
    list-style: none; display: flex; flex-direction: column; gap: 16px;
  }
  .contact { display: flex; align-items: center; gap: 14px; font-size: 18px; color: var(--white); }
  .contact-icon {
    width: 32px; height: 32px; border-radius: 50%;
    border: 1.5px solid var(--cyan);
    display: flex; align-items: center; justify-content: center;
  }
  .contact-icon svg { width: 16px; height: 16px; }

  /* back */
  .services {
    position: absolute; left: 44px; right: 36px; top: 22px; bottom: 22px;
    display: flex; flex-direction: column;
  }
  .service {
    flex: 1;
    display: flex; align-items: center; gap: 24px;
    border-bottom: 1px solid var(--divider);
  }
  .service:last-child { border-bottom: none; }
  .service-text { flex: 1; }
  .service-title {
    font-size: 18px; font-weight: 700; color: var(--cyan);
    letter-spacing: 1.5px; text-transform: uppercase; margin-bottom: 5px;
  }
  .service--full .service-title { color: var(--violet-light); }
  .service-desc { font-size: 13.5px; line-height: 18px; color: var(--soft); }
  .price {
    width: 104px; flex: none;
    text-align: center;
    font-size: 30px; font-weight: 700; color: var(--white);
    padding: 10px 0;
    border-radius: 12px;
    border: 2px solid var(--cyan);
  }
  .service--full .price {
    border: none;
    background: linear-gradient(135deg, var(--violet), var(--crimson));
  }
</style>
</head>
<body>
  <section class="card card--front">
    <svg class="stripes" viewBox="0 0 300 392" aria-hidden="true">
      <g stroke="var(--teal-line)" stroke-width="22">
        <line x1="120" y1="420" x2="340" y2="-20"/>
        <line x1="180" y1="420" x2="400" y2="-20"/>
        <line x1="240" y1="420" x2="460" y2="-20"/>
      </g>
    </svg>
    <div class="accent-band"></div>
    <div class="brand">
      <span class="brand-dot"></span>
      <span class="brand-name">SHORELINE DETAILING</span>
    </div>
    <h1 class="owner-name">DANE WHITLOCK</h1>
    <p class="owner-role">Owner Operator</p>
    <div class="name-rule"></div>
    <ul class="contacts">
      <li class="contact">
        <span class="contact-icon">
          <svg viewBox="0 0 24 24" fill="none" stroke="#3cc4e6" stroke-width="2.2" stroke-linejoin="round"><path d="M5 3h4l2 5-2.5 1.5a11 11 0 0 0 6 6L16 13l5 2v4a2 2 0 0 1-2 2A17 17 0 0 1 3 5a2 2 0 0 1 2-2z"/></svg>
        </span>
        0400 123 456
      </li>
      <li class="contact">
        <span class="contact-icon">
          <svg viewBox="0 0 24 24" fill="none" stroke="#3cc4e6" stroke-width="2.2" stroke-linejoin="round"><rect x="3" y="5" width="18" height="14" rx="2"/><path d="M3 7l9 6 9-6"/></svg>
        </span>
        shorelinedetailing@example.com
      </li>
    </ul>
  </section>

  <section class="card card--back">
    <div class="accent-band"></div>
    <div class="services">
      <div class="service">
        <div class="service-text">
          <h2 class="service-title">Interior Detail</h2>
          <p class="service-desc">Vacuum &amp; deep clean of carpets &amp; upholstery or leather treatment, interior trim clean &amp; condition, window polish &amp; treatment, steam clean and stain removal</p>
        </div>
        <div class="price">$150</div>
      </div>
      <div class="service">
        <div class="service-text">
          <h2 class="service-title">Exterior Detail</h2>
          <p class="service-desc">Extreme wash &amp; polish, exterior trim reviver &amp; protector, window polish &amp; treatment, tyre dressing, engine bay cleaned</p>
        </div>
        <div class="price">$250</div>
      </div>
      <div class="service service--full">
        <div class="service-text">
          <h2 class="service-title">Full Extreme Detail</h2>
          <p class="service-desc">Extreme wash &amp; polish, tyre dressing, engine bay cleaned, vacuum &amp; deep clean of carpets &amp; upholstery or leather treatment, interior &amp; exterior trim reviver &amp; protector, window polish &amp; treatment</p>
        </div>
        <div class="price">$350</div>
      </div>
    </div>
  </section>
</body>
</html>
```